Educational Software Company Needs Banner Ads Prompting an Event

We are looking for a series of banner ads (to be used in conjunction with google adwords), pushing people to register for our upcoming road tour, Faculty Trailblazers. Faculty Trailblazers is a series of one-day workshops that offer best practices for individuals in the educational operations industry. To learn more about the event please view the website at: facultytrailblazers.learnwick.example.

Feel free to use any of the language from the website, logo (attached), and the hex colors which are listed in the "must have" section below.

Some language that we have use on other marketing materials:
"We're Hitting the Road!"
Our 2014 road tour is heading to a city near you!
"Invest in Your Success"
"We're Hitting the Road, and Heading Your Way!"
"Faculty Trailblazers - A free, one-day workshop offering lessons for success"
"Seating is Limited - Register Today!"

Supported ad sizes and specs:
250 x 250 square
200 x 200 square
468 x 60 banner
728 x 90 leaderboard
300 x 250 inline rectangle
120 x 600 skyscraper
160 x 600 wide skyscrapper
320 x 50 mobile leaderboard

The call to action for the ad should be to "Register Today!"

Target Market(s)

educational operations professionals, i.e. maintenance directors, energy managers, superintendents, business officers etc...

Industry/Entity Type

Marketing

Requirements
Must have
• event logo and/or event name using event colors; CTA button reading "Register Today!"

Colors:
FT – Red #A63515
R: 166
G: 53
B: 21

FT – Dark Gray #726658
R: 114
G: 102
B: 88

FT – Light Gray #CECECE
R: 206
G: 206
B: 206

FT – Orange #EDA45B
R: 237
G: 164
B: 91
Nice to have
• Consider using list of stops on larger banner ads.

1/14/2014 Seattle, CA
1/16/2014 Phoenix, CA
1/21/2014 Sacramento, CA
1/23/2014 Ontario, CA
2/13/2014 Kilgore, TX
2/11/2014 Coppell, TX
TBD Schaumburg, IL

```html
<!DOCTYPE html>
<html lang="en">
<head>
<meta charset="utf-8">
<title>Faculty Trailblazers – Banner Ad Set</title>
<link href="https://fonts.googleapis.com/css2?family=Bree+Serif&display=swap" rel="stylesheet">
<style>
:root{
  --ft-red:#A63515;
  --ft-dark-gray:#726658;
  --ft-light-gray:#CECECE;
  --ft-orange:#EDA45B;
  --sky:#AADDDC;
  --paper:#FFFFFF;
  --stage:#000000;
  --hill:#8BA56E;
  --road:#6E6354;
}
*{box-sizing:border-box;margin:0;padding:0}
html,body{width:1200px;height:623px;overflow:hidden;background:var(--stage)}
body{position:relative;font-family:"Bree Serif",Georgia,serif;color:var(--ft-red)}

.ad{position:absolute;background:var(--sky);overflow:hidden}
.ad--sky-a{left:37px;top:5px;width:160px;height:598px}
.ad--sky-b{left:208px;top:5px;width:160px;height:598px}
.ad--leader-a{left:386px;top:8px;width:727px;height:88px}
.ad--leader-b{left:386px;top:112px;width:727px;height:89px}
.ad--rect-a{left:386px;top:222px;width:299px;height:249px}
.ad--rect-b{left:699px;top:222px;width:299px;height:249px}

/* event name lockup */
.event-name{position:absolute;display:flex;flex-direction:column;align-items:center;text-align:center;color:var(--ft-red);line-height:1.02}
.event-name__dot{width:26px;height:26px;border-radius:50%;background:var(--ft-orange);margin-bottom:8px}
.event-name__text{font-size:25px}
.event-name--lg{left:0;width:160px;top:16px}
.event-name--md{left:10px;width:100px;top:22px}
.event-name--md .event-name__text{font-size:19px}
.event-name--md .event-name__dot{width:22px;height:22px}
.event-name--sm{left:6px;width:72px;top:10px}
.event-name--sm .event-name__text{font-size:13px}
.event-name--sm .event-name__dot{width:14px;height:14px;margin-bottom:5px}

/* headline */
.headline{position:absolute;text-align:center;font-size:21px;line-height:26px;color:var(--ft-red)}
.headline b{font-weight:400;font-size:22px;text-shadow:0 0 .5px var(--ft-red)}
.headline--sky{left:0;width:160px;top:177px}
.headline--rect{left:130px;width:162px;top:6px;font-size:21px;line-height:25px}
.headline--leader{left:110px;width:350px;top:21px;font-size:18px;line-height:22px}
.headline--leader b{font-size:18px}

/* call to action */
.cta{position:absolute;border-radius:50%;background:var(--ft-red);color:var(--ft-orange);display:flex;align-items:center;justify-content:center;text-align:center;font-size:16px;line-height:19px;box-shadow:0 0 0 3px var(--ft-red),inset 0 0 0 2px rgba(237,164,91,.35)}
.cta--lg{width:80px;height:80px;left:36px;top:392px}
.cta--md{width:78px;height:78px}
.cta--sm{width:66px;height:66px;font-size:13px;line-height:16px}

/* illustration placeholder */
.scene{position:absolute;background:linear-gradient(180deg,var(--sky) 0%,#9CC7B8 35%,var(--hill) 62%,var(--road) 80%,#7D9A4E 100%)}
.scene--sky{left:0;top:488px;width:160px;height:110px}
.scene--rect{left:0;top:150px;width:299px;height:99px}
.scene--leader{right:0;top:0;width:250px;height:100%;background:linear-gradient(90deg,var(--sky) 0%,#A5C9B6 25%,var(--hill) 55%,#7D9A4E 100%)}

/* destination list */
.ribbon{position:absolute}
.ribbon__label{position:absolute;inset:0;display:flex;align-items:center;justify-content:center;color:var(--ft-orange);font-size:17px;letter-spacing:.3px}
.stops{position:absolute;background:var(--paper);clip-path:polygon(0 0,100% 0,100% 88%,50% 100%,0 88%);text-align:center;font-size:12.5px;line-height:16px;color:var(--ft-red);list-style:none}
.stops--sky{left:16px;top:236px;width:126px;height:147px;padding-top:10px}
.stops--rect{left:137px;top:34px;width:128px;height:148px;padding-top:11px}

.dest-panel{position:absolute;left:114px;top:0;width:345px;height:89px}
.dest-panel__title{position:absolute;left:26px;top:8px;font-size:17px;color:var(--ft-dark-gray);letter-spacing:.3px}
.dest-panel__grid{position:absolute;left:30px;top:36px;display:grid;grid-template-columns:90px 113px 80px;list-style:none;font-size:12.5px;line-height:16px;color:var(--ft-red)}
</style>
</head>
<body>

<!-- 160 x 600 skyscraper, headline -->
<section class="ad ad--sky-a" aria-label="Wide skyscraper ad">
  <div class="event-name event-name--lg"><span class="event-name__dot"></span><span class="event-name__text">Faculty<br>Trailblazers</span></div>
  <p class="headline headline--sky">A free,<br><b>one-day</b><br>workshop for<br>education<br>operations<br>professionals</p>
  <div class="cta cta--lg">Register<br>Today!</div>
  <div class="scene scene--sky" role="img" aria-label="Illustration of a red station wagon piled with luggage driving a mountain road"></div>
</section>

<!-- 160 x 600 skyscraper, destinations -->
<section class="ad ad--sky-b" aria-label="Wide skyscraper ad with tour stops">
  <div class="event-name event-name--lg"><span class="event-name__dot"></span><span class="event-name__text">Faculty<br>Trailblazers</span></div>
  <svg class="ribbon" style="left:0;top:203px" width="160" height="42" viewBox="0 0 160 42" aria-hidden="true">
    <rect x="0" y="0" width="160" height="34" fill="#A63515"/>
    <polygon points="0,34 16,34 16,42" fill="#6E2410"/>
    <polygon points="160,34 144,34 144,42" fill="#6E2410"/>
  </svg>
  <div class="ribbon__label" style="top:203px;height:34px;bottom:auto">DESTINATION</div>
  <ul class="stops stops--sky"><li>Seattle, CA</li><li>Phoenix, CA</li><li>Sacramento, CA</li><li>Ontario, CA</li><li>Kilgore, TX</li><li>Coppell, TX</li></ul>
  <div class="cta cta--lg">Register<br>Today!</div>
  <div class="scene scene--sky" role="img" aria-label="Illustration of a red station wagon piled with luggage driving a mountain road"></div>
</section>

<!-- 728 x 90 leaderboard, headline -->
<section class="ad ad--leader-a" aria-label="Leaderboard ad">
  <div class="scene scene--leader" role="img" aria-label="Illustration of a red station wagon piled with luggage on a road past mountains and pine trees"></div>
  <div class="event-name event-name--sm"><span class="event-name__dot"></span><span class="event-name__text">Faculty<br>Trailblazers</span></div>
  <p class="headline headline--leader">A free, <b>one-day</b> workshop<br>for education operations professionals</p>
  <div class="cta cta--sm" style="left:446px;top:11px">Register<br>Today!</div>
</section>

<!-- 728 x 90 leaderboard, destinations -->
<section class="ad ad--leader-b" aria-label="Leaderboard ad with tour stops">
  <div class="scene scene--leader" role="img" aria-label="Illustration of a red station wagon piled with luggage on a road past mountains and pine trees"></div>
  <div class="event-name event-name--sm"><span class="event-name__dot"></span><span class="event-name__text">Faculty<br>Trailblazers</span></div>
  <svg class="dest-panel" viewBox="0 0 345 89" aria-hidden="true">
    <rect x="0" y="0" width="12" height="89" fill="#A63515"/>
    <polygon points="12,4 345,4 312,45 345,86 12,86" fill="#FFFFFF"/>
    <line x1="150" y1="17" x2="292" y2="17" stroke="#A63515" stroke-width="1.5"/>
  </svg>
  <div class="dest-panel" aria-label="Tour stops">
    <p class="dest-panel__title">DESTINATION</p>
    <ul class="dest-panel__grid"><li>Seattle, CA</li><li>Ontario, CA</li><li>Kilgore, TX</li><li>Phoenix, CA</li><li>Sacramento, CA</li><li>Coppell, TX</li></ul>
  </div>
  <div class="cta cta--sm" style="left:447px;top:13px">Register<br>Today!</div>
</section>

<!-- 300 x 250 rectangle, headline -->
<section class="ad ad--rect-a" aria-label="Inline rectangle ad">
  <div class="scene scene--rect" role="img" aria-label="Illustration of a red station wagon piled with luggage driving a mountain road"></div>
  <div class="event-name event-name--md"><span class="event-name__dot"></span><span class="event-name__text">Faculty<br>Trailblazers</span></div>
  <p class="headline headline--rect">A free,<br><b>one-day</b><br>workshop for<br>education<br>operations<br>professionals</p>
  <div class="cta cta--md" style="left:168px;top:166px">Register<br>Today!</div>
</section>

<!-- 300 x 250 rectangle, destinations -->
<section class="ad ad--rect-b" aria-label="Inline rectangle ad with tour stops">
  <div class="scene scene--rect" role="img" aria-label="Illustration of a red station wagon piled with luggage driving a mountain road"></div>
  <div class="event-name event-name--md"><span class="event-name__dot"></span><span class="event-name__text">Faculty<br>Trailblazers</span></div>
  <ul class="stops stops--rect"><li>Seattle, CA</li><li>Phoenix, CA</li><li>Sacramento, CA</li><li>Ontario, CA</li><li>Kilgore, TX</li><li>Coppell, TX</li></ul>
  <svg class="ribbon" style="left:104px;top:5px" width="195" height="44" viewBox="0 0 195 44" aria-hidden="true">
    <polygon points="0,10 20,10 14,24 20,38 0,38" fill="#8A2B11"/>
    <polygon points="195,10 175,10 181,24 175,38 195,38" fill="#8A2B11"/>
    <rect x="18" y="0" width="159" height="34" fill="#A63515"/>
    <polygon points="18,34 32,34 32,42" fill="#6E2410"/>
    <polygon points="177,34 163,34 163,42" fill="#6E2410"/>
  </svg>
  <div class="ribbon__label" style="left:122px;width:159px;top:5px;height:34px;right:auto;bottom:auto">DESTINATION</div>
  <div class="cta cta--md" style="left:163px;top:166px">Register<br>Today!</div>
</section>

</body>
</html>
```